Bref créative
Business Cards/Letterhead for a Private Equity Real Estate Company
KTR Commercial
Simple
H. Dalton Greave
President
4780 Brambling Road
Suite 610
Atlanta, GA 30342
dalton@ktrcommercial.net
http://ktrcommercial.net/
We think we want the logo on one side and then all the written information on the other. Open to seeing different suggestions, though. Thanks for everyone who participates!

```html
<!DOCTYPE html>
<html lang="en">
<head>
<meta charset="utf-8">
<title>KTR Commercial — Business Card</title>
<link href="https://fonts.googleapis.com/css2?family=Open+Sans:wght@400;600;700&display=swap" rel="stylesheet">
<style>
  :root {
    --backdrop: #e7e5e2;
    --card-white: #ffffff;
    --slate-dark: #575757;
    --slate-mid: #6e6e6e;
    --slate-light: #8a8a8a;
    --ink: #3f3f3f;
    --accent-red: #b8252c;
    --text-light: #f4f4f4;
    --shadow: rgba(0, 0, 0, 0.22);
  }
  * { margin: 0; padding: 0; box-sizing: border-box; }
  html, body {
    width: 1200px;
    height: 988px;
    overflow: hidden;
    background: var(--backdrop);
    font-family: "Open Sans", Arial, sans-serif;
  }
  .canvas {
    position: relative;
    width: 1200px;
    height: 988px;
  }
  .card {
    position: absolute;
    left: 215px;
    width: 770px;
    height: 440px;
    box-shadow: 0 10px 28px var(--shadow);
    overflow: hidden;
  }

  /* Back side */
  .card-back {
    top: 24px;
    background: linear-gradient(160deg, var(--slate-light) 0%, var(--slate-mid) 45%, var(--slate-dark) 100%);
    display: flex;
    flex-direction: column;
    align-items: center;
    justify-content: center;
  }
  .wordmark {
    font-weight: 600;
    letter-spacing: 0.08em;
    text-transform: uppercase;
    display: flex;
    align-items: center;
    gap: 16px;
  }
  .wordmark-mark {
    width: 22px;
    height: 22px;
  }
  .card-back .wordmark { color: var(--text-light); font-size: 46px; }
  .card-back .wordmark-mark { background: var(--text-light); }
  .card-back .website-line {
    margin-top: 34px;
    color: var(--text-light);
    font-size: 13px;
    letter-spacing: 0.55em;
  }

  /* Front side */
  .card-front {
    top: 524px;
    background: var(--card-white);
  }
  .front-brand {
    position: absolute;
    top: 0;
    left: 0;
    width: 100%;
    height: 214px;
    display: flex;
    flex-direction: column;
    align-items: center;
    justify-content: center;
  }
  .card-front .wordmark { color: var(--slate-dark); font-size: 40px; }
  .card-front .wordmark-mark { background: var(--slate-dark); width: 19px; height: 19px; }
  .tagline {
    margin-top: 10px;
    color: var(--accent-red);
    font-size: 10px;
    letter-spacing: 0.3em;
    text-transform: uppercase;
  }
  .divider-red {
    position: absolute;
    top: 214px;
    left: 0;
    width: 100%;
    height: 3px;
    background: var(--accent-red);
  }
  .contact-band {
    position: absolute;
    top: 220px;
    left: 0;
    width: 100%;
    height: 220px;
    background: linear-gradient(180deg, var(--slate-light) 0%, var(--slate-mid) 100%);
    display: flex;
    justify-content: center;
    align-items: center;
    color: var(--text-light);
  }
  .person {
    text-align: right;
    padding-right: 22px;
    font-size: 15px;
    line-height: 1.55;
  }
  .person-name { font-weight: 700; font-size: 18px; }
  .person-title { margin-bottom: 10px; }
  .column-rule {
    width: 1px;
    height: 124px;
    background: var(--text-light);
    opacity: 0.8;
  }
  .contact-list {
    list-style: none;
    padding-left: 22px;
    font-size: 15px;
  }
  .contact-list li {
    display: flex;
    align-items: center;
    gap: 10px;
    height: 29px;
  }
  .contact-icon { width: 20px; height: 20px; flex: none; }
</style>
</head>
<body>
<main class="canvas">

  <section class="card card-back" aria-label="Business card, back">
    <div class="wordmark"><span class="wordmark-mark"></span>KTR Commercial</div>
    <p class="website-line">www.ktrcommercial.net</p>
  </section>

  <section class="card card-front" aria-label="Business card, front">
    <div class="front-brand">
      <div class="wordmark"><span class="wordmark-mark"></span>KTR Commercial</div>
      <p class="tagline">Acquisition • Development • Management</p>
    </div>
    <div class="divider-red"></div>
    <div class="contact-band">
      <div class="person">
        <p class="person-name">H. Dalton Greave</p>
        <p class="person-title">President</p>
        <p>4780 Brambling Road</p>
        <p>Suite 610 Atlanta, GA 30342</p>
      </div>
      <div class="column-rule"></div>
      <ul class="contact-list">
        <li>
          <svg class="contact-icon" viewBox="0 0 20 20" aria-hidden="true">
            <circle cx="10" cy="10" r="10" fill="#f4f4f4"/>
            <path d="M6.5 5.5l2 0 1 2.5-1.3 1a6 6 0 0 0 2.8 2.8l1-1.3 2.5 1v2c0 .6-.5 1-1 1A8 8 0 0 1 5.5 6.5c0-.5.4-1 1-1z" fill="#6e6e6e"/>
          </svg>
          (404) 555-0172
        </li>
        <li>
          <svg class="contact-icon" viewBox="0 0 20 20" aria-hidden="true">
            <circle cx="10" cy="10" r="10" fill="#f4f4f4"/>
            <rect x="7" y="4.5" width="6" height="11" rx="1" fill="#6e6e6e"/>
            <rect x="8" y="6" width="4" height="7" fill="#f4f4f4"/>
          </svg>
          (404) 555-0839
        </li>
        <li>
          <svg class="contact-icon" viewBox="0 0 20 20" aria-hidden="true">
            <circle cx="10" cy="10" r="10" fill="#f4f4f4"/>
            <rect x="5" y="6.5" width="10" height="7" fill="#6e6e6e"/>
            <path d="M5 6.5l5 4 5-4" fill="none" stroke="#f4f4f4" stroke-width="1"/>
          </svg>
          dalton@ktrcommercial.net
        </li>
        <li>
          <svg class="contact-icon" viewBox="0 0 20 20" aria-hidden="true">
            <circle cx="10" cy="10" r="10" fill="#f4f4f4"/>
            <circle cx="10" cy="10" r="5.5" fill="none" stroke="#6e6e6e" stroke-width="1.2"/>
            <ellipse cx="10" cy="10" rx="2.4" ry="5.5" fill="none" stroke="#6e6e6e" stroke-width="1"/>
            <path d="M4.5 10h11" stroke="#6e6e6e" stroke-width="1"/>
          </svg>
          www.ktrcommercial.net
        </li>
      </ul>
    </div>
  </section>

</main>
</body>
</html>
```